Successful Software Co Launching A Super FUN Mobile & Web Application - ROCKSTAR Designer Needed

Our App is called "Brightly Tally"It is an employee "gamification" app designed to make working at your job fun...Employees complete simple tasks throughout the work day and are rewarded with points they can redeem for different gifts and benefits...We an AMAZING User Interface designed for both the mobile app and website app. We are looking for a clean, modern and simple design... This app is designed to make employees more engaged at work while having fun doing the things they already do each day...They can then redeem their points for rewards. It needs to be easy to understand and simple in its design...Example: A local carpet cleaning business uses our app.Their employees show up to work on time - They get 50 pointsThey clean out their work vehicle - They get 100 pointsThey up-sell an additional cleaning job - The get 250 pointsEtc...The app will also have fun icons and graphics that appear on the screen when an employee accomplishes a task.The app will play fun music sounds when they accomplish tasks too.
Updates

Need extra days to review

Target Market(s)

Small business owners

Logo Text

Brightly Tally

Font styles to use
Sans Serif

Colors

Designer to choose colors to be used in the design.

Requirements
Must have
• Simple elegant design
Nice to have
• I'd like to see examples of fun "icons" that could pop up on the screen after an employee completes a "task" and earns points... Something fun to pop up on the screen... (like a happy face, a thumbs up, fun text bubbles... "Way To Go!" etc... or any other fun ideas)

```html
<!DOCTYPE html>
<html lang="en">
<head>
<meta charset="utf-8">
<title>Brightly Tally – Mobile Screens</title>
<link href="https://fonts.googleapis.com/css2?family=Nunito+Sans:wght@400;600;700;800;900&display=swap" rel="stylesheet">
<style>
  :root{
    --canvas:#f3f4f6;
    --screen:#ffffff;
    --sky:#e8f5fd;
    --sky-deep:#d3ecfb;
    --blue:#1aa0e3;
    --blue-dark:#0b86c9;
    --orange:#f7962f;
    --orange-dark:#f27420;
    --purple:#9a5bd6;
    --purple-dark:#7940c2;
    --ink:#24303d;
    --muted:#8a96a3;
    --line:#e6eaee;
  }
  *{box-sizing:border-box;margin:0;padding:0}
  html,body{width:872px;height:1200px;overflow:hidden}
  body{background:var(--canvas);font-family:"Nunito Sans",Arial,sans-serif;color:var(--ink);position:relative}
  .screen{position:absolute;width:360px;height:560px;background:var(--screen);border-radius:26px;overflow:hidden;box-shadow:0 10px 30px rgba(30,50,70,.12)}
  .screen--home{left:38px;top:30px}
  .screen--redeem{left:474px;top:30px}
  .screen--success{left:38px;top:620px}
  .screen--menu{left:474px;top:620px}
  .status{position:absolute;top:8px;left:22px;right:22px;display:flex;justify-content:space-between;font-size:10px;font-weight:700;z-index:5}
  .status__icons{display:flex;gap:4px;align-items:center}
  .status__icons i{display:block;background:currentColor;border-radius:1px}
  .menu-icon{position:absolute;top:34px;left:18px;width:18px;z-index:5}
  .menu-icon span{display:block;height:2px;background:var(--blue);margin-bottom:4px;border-radius:2px}
  .wave-band{position:absolute;left:0;top:0;width:100%}
  .btn{display:flex;align-items:center;justify-content:center;gap:8px;height:36px;border-radius:18px;background:var(--blue);color:#fff;font-size:12px;font-weight:700;position:absolute;left:50px;right:50px}
  .btn .dot{width:14px;height:14px;border:2px solid #fff;border-radius:50%}
  /* home */
  .welcome{position:absolute;top:32px;width:100%;text-align:center}
  .welcome__hi{font-size:14px;color:var(--ink);font-weight:600}
  .welcome__name{font-size:18px;color:var(--blue);font-weight:800}
  .points-ring{position:absolute;left:50%;transform:translateX(-50%);border-radius:50%;background:#fff;display:flex;flex-direction:column;align-items:center;justify-content:center}
  .points-ring svg{position:absolute;inset:0}
  .points-ring__value{font-weight:900;line-height:1}
  .points-ring__label{font-size:10px;color:var(--muted);font-weight:700}
  .points-ring__sub{font-size:7px;color:var(--muted)}
  .grabs{position:absolute;top:264px;width:100%;text-align:center;font-size:11px;font-weight:800}
  .reward-card{position:absolute;left:16px;right:16px;height:112px;border-radius:10px;color:#fff;padding:14px 16px;overflow:hidden}
  .reward-card--orange{background:linear-gradient(135deg,var(--orange),var(--orange-dark))}
  .reward-card--purple{background:linear-gradient(135deg,var(--purple),var(--purple-dark))}
  .reward-card__pts{font-size:22px;font-weight:900;line-height:1}
  .reward-card__need{font-size:9px;font-weight:700;opacity:.9}
  .reward-card__title{position:absolute;left:16px;bottom:14px;font-size:17px;font-weight:800}
  .reward-card__shape{position:absolute;right:-20px;top:-10px;width:150px;height:150px;border-radius:50%;background:rgba(255,255,255,.1)}
  /* redeem */
  .page-title{position:absolute;top:30px;width:100%;text-align:center;font-size:16px;font-weight:800}
  .progress-note{position:absolute;top:62px;left:86px;right:20px;font-size:11px;color:var(--ink);font-weight:600;line-height:1.35}
  .progress-note b{color:var(--blue)}
  .task-card{position:absolute;left:16px;right:16px;height:128px;border-radius:10px;background:linear-gradient(135deg,var(--blue),var(--blue-dark));color:#fff;padding:14px 16px}
  .task-card__pts{font-size:22px;font-weight:900}
  .task-card__pts small{font-size:10px;font-weight:700;margin-left:3px}
  .task-card__title{font-size:17px;font-weight:800;line-height:1.2;margin-top:4px;max-width:260px}
  .task-card__btn{position:absolute;left:16px;bottom:12px;font-size:10px;font-weight:800;background:rgba(255,255,255,.25);border-radius:12px;padding:4px 14px}
  /* success */
  .burst{position:absolute;top:0;left:0;width:100%;height:300px}
  .burst__text{position:absolute;top:100px;width:100%;text-align:center;color:#fff}
  .burst__value{font-size:64px;font-weight:900;line-height:1}
  .burst__label{font-size:18px;font-weight:700}
  .congrats{position:absolute;top:340px;width:100%;text-align:center;padding:0 40px}
  .congrats h2{font-size:22px;font-weight:900}
  .congrats p{margin-top:10px;font-size:13px;color:var(--muted);line-height:1.45}
  /* menu */
  .dim{position:absolute;inset:0;background:rgba(36,48,61,.35)}
  .drawer{position:absolute;left:0;top:0;bottom:0;width:250px;background:#fff;padding:70px 0 0 24px}
  .drawer__close{position:absolute;top:30px;right:20px;width:18px;height:18px}
  .drawer__item{display:flex;align-items:center;gap:8px;font-size:13px;font-weight:700;height:36px;color:var(--ink)}
  .drawer__item--active{color:var(--blue)}
  .drawer__item--active i{width:10px;height:10px;border-radius:50%;background:var(--blue)}
</style>
</head>
<body>

<!-- Home -->
<section class="screen screen--home">
  <div class="status"><span>09:41</span><span class="status__icons"><i style="width:14px;height:7px"></i><i style="width:18px;height:8px;border-radius:2px"></i></span></div>
  <svg class="wave-band" height="250" viewBox="0 0 360 250" preserveAspectRatio="none"><path d="M0 0H360V200C300 240 240 170 170 205C100 240 50 220 0 200Z" fill="var(--sky)"/><path d="M0 215C70 240 120 200 190 222C260 245 310 215 360 210V250H0Z" fill="var(--sky-deep)" opacity=".6"/></svg>
  <div class="menu-icon"><span></span><span></span><span></span></div>
  <div class="welcome"><div class="welcome__hi">Welcome to</div><div class="welcome__name">Brightly Tally, Jamie</div></div>
  <div class="points-ring" style="top:86px;width:112px;height:112px">
    <svg viewBox="0 0 112 112"><circle cx="56" cy="56" r="51" fill="none" stroke="var(--line)" stroke-width="6"/><circle cx="56" cy="56" r="51" fill="none" stroke="var(--blue)" stroke-width="6" stroke-dasharray="240 400" stroke-linecap="round" transform="rotate(-90 56 56)"/></svg>
    <span class="points-ring__value" style="font-size:26px">2,250</span>
    <span class="points-ring__label">Points</span>
    <span class="points-ring__sub">to next reward</span>
  </div>
  <div class="btn" style="top:214px"><span class="dot"></span>Choose your rewards</div>
  <div class="grabs">Up for grabs ⌄</div>
  <div class="reward-card reward-card--orange" style="top:290px"><span class="reward-card__shape"></span><div class="reward-card__pts">500</div><div class="reward-card__need">Points needed</div><div class="reward-card__title">$15 Beanhouse Card</div></div>
  <div class="reward-card reward-card--purple" style="top:414px"><span class="reward-card__shape"></span><div class="reward-card__pts">1,000</div><div class="reward-card__need">Points needed</div><div class="reward-card__title">$25 Techmart Voucher</div></div>
</section>

<!-- Redeem -->
<section class="screen screen--redeem">
  <div class="status"><span>09:41</span><span class="status__icons"><i style="width:14px;height:7px"></i><i style="width:18px;height:8px;border-radius:2px"></i></span></div>
  <svg class="wave-band" height="125" viewBox="0 0 360 125" preserveAspectRatio="none"><path d="M0 0H360V100C300 125 230 85 160 108C90 130 40 115 0 105Z" fill="var(--sky)"/></svg>
  <div class="menu-icon"><span></span><span></span><span></span></div>
  <div class="page-title">Redeem</div>
  <div class="points-ring" style="top:56px;left:46px;width:54px;height:54px">
    <svg viewBox="0 0 54 54"><circle cx="27" cy="27" r="24" fill="none" stroke="var(--line)" stroke-width="3"/><circle cx="27" cy="27" r="24" fill="none" stroke="var(--blue)" stroke-width="3" stroke-dasharray="110 200" transform="rotate(-90 27 27)"/></svg>
    <span class="points-ring__value" style="font-size:12px">2,250</span>
    <span class="points-ring__sub">Points</span>
  </div>
  <p class="progress-note">You are only <b>750 points</b> away from your next reward</p>
  <div class="task-card" style="top:132px"><div class="task-card__pts">100<small>Points</small></div><div class="task-card__title">Show up on time every day for 1 month</div><span class="task-card__btn">Redeem</span></div>
  <div class="task-card" style="top:272px"><div class="task-card__pts">250<small>Points</small></div><div class="task-card__title">Up-sell over $250 in services</div><span class="task-card__btn">Redeem</span></div>
  <div class="task-card" style="top:412px"><div class="task-card__pts">50<small>Points</small></div><div class="task-card__title">Pass your vehicle inspection each week</div><span class="task-card__btn">Redeem</span></div>
</section>

<!-- Success -->
<section class="screen screen--success">
  <div class="status" style="color:#fff"><span>09:41</span><span class="status__icons"><i style="width:14px;height:7px"></i><i style="width:18px;height:8px;border-radius:2px"></i></span></div>
  <svg class="burst" viewBox="0 0 360 300" preserveAspectRatio="none"><defs><linearGradient id="orangeFill" x1="0" y1="0" x2="1" y2="1"><stop offset="0" stop-color="#f9a640"/><stop offset="1" stop-color="#f27420"/></linearGradient></defs><path d="M0 0H360V250C290 295 220 230 150 265C90 295 40 280 0 262Z" fill="url(#orangeFill)"/></svg>
  <div class="burst__text"><div class="burst__value">500</div><div class="burst__label">Points earned!</div></div>
  <div class="congrats"><h2>Congratulations, Jamie!</h2><p>You completed a task and earned 500 points</p></div>
  <div class="btn" style="top:470px"><span class="dot"></span>Choose your rewards</div>
</section>

<!-- Menu -->
<section class="screen screen--menu">
  <svg class="wave-band" height="250" viewBox="0 0 360 250" preserveAspectRatio="none"><path d="M0 0H360V200C300 240 240 170 170 205C100 240 50 220 0 200Z" fill="var(--sky)"/></svg>
  <div class="reward-card reward-card--orange" style="top:290px"></div>
  <div class="reward-card reward-card--purple" style="top:414px"></div>
  <div class="dim"></div>
  <nav class="drawer">
    <svg class="drawer__close" viewBox="0 0 18 18"><path d="M3 3L15 15M15 3L3 15" stroke="var(--blue)" stroke-width="2.2" stroke-linecap="round"/></svg>
    <div class="drawer__item drawer__item--active"><i></i>Your Rewards</div>
    <div class="drawer__item">Redeem Points</div>
    <div class="drawer__item">Reward History</div>
    <div class="drawer__item">Request Time Off</div>
    <div class="drawer__item">Contact Employer</div>
  </nav>
</section>

</body>
</html>
```